Request for Business Card Design

Hi. My name is Marlena, I am looking for a new business card design for my company, Quorvane Sensing Systems, LLC. I really like the design you did for Tessaly Harvest and was hoping you could do something similar using our full logo and our mark. I am also open to any raised texture design using our mark. I have attached our full logo, which would need to be somewhere on the card, as well as the mark in both outline and full form, as well as our brand colors / guide. The card does not have to be white, as long as our logo and mark appear. I actually like darker colored business cards more, but am open to all options. If you are interested in working with me, please let me know. We would also take the business card design into letterhead design if you can do that.

```html
<!DOCTYPE html>
<html lang="en">
<head>
<meta charset="utf-8">
<title>Quorvane Sensing Systems — Business Card</title>
<link rel="stylesheet" href="https://fonts.googleapis.com/css2?family=Lato:wght@400;700;900&display=swap">
<style>
  :root {
    --bg: #1e1e1e;
    --card-dark: #3d3d3f;
    --card-light: #ffffff;
    --brand-blue: #0399c0;
    --ink: #2a2a2a;
    --silver: #b9b9bb;
  }
  * { box-sizing: border-box; margin: 0; padding: 0; }
  html, body { width: 1200px; height: 875px; overflow: hidden; }
  body {
    background: var(--bg);
    font-family: "Lato", sans-serif;
    position: relative;
  }
  .card {
    position: absolute;
    width: 560px;
    height: 320px;
    border-radius: 22px;
    overflow: hidden;
  }
  /* Front: dark card */
  .card--front {
    left: 50px; top: 95px;
    background: var(--card-dark);
  }
  .front-logo {
    position: absolute;
    left: 60px; top: 132px;
    display: flex; align-items: center; gap: 18px;
  }
  .front-logo__dot {
    width: 48px; height: 48px; border-radius: 50%;
    background: var(--brand-blue);
  }
  .front-logo__name {
    font-weight: 900;
    font-size: 27px;
    letter-spacing: 3px;
    color: var(--silver);
    text-transform: uppercase;
  }
  /* Back: white card */
  .card--back {
    left: 600px; top: 470px;
    background: var(--card-light);
  }
  .back-accent {
    position: absolute;
    left: -170px; top: 120px;
    width: 380px; height: 380px;
    border-radius: 50%;
    background: var(--brand-blue);
  }
  .contact {
    position: absolute;
    right: 34px; top: 34px;
    text-align: right;
  }
  .contact__name {
    font-weight: 900;
    font-size: 30px;
    color: var(--brand-blue);
    text-transform: uppercase;
    letter-spacing: 0.5px;
    line-height: 1;
  }
  .contact__title {
    font-size: 17px;
    color: var(--ink);
    margin-top: 4px;
    margin-bottom: 22px;
  }
  .contact__list { list-style: none; }
  .contact__item {
    display: flex; justify-content: flex-end; align-items: center; gap: 10px;
    font-size: 14.5px;
    color: var(--ink);
    line-height: 24px;
  }
  .contact__item--plain { padding-right: 24px; }
  .icon { width: 14px; height: 14px; fill: var(--brand-blue); flex: none; }
</style>
</head>
<body>

  <section class="card card--front" aria-label="Card front">
    <div class="front-logo">
      <span class="front-logo__dot"></span>
      <span class="front-logo__name">Quorvane Sensing Systems</span>
    </div>
  </section>

  <section class="card card--back" aria-label="Card back">
    <div class="back-accent" role="img" aria-label="Large brand-blue accent shape"></div>
    <div class="contact">
      <h1 class="contact__name">Daniel Ashcombe</h1>
      <p class="contact__title">Founder &amp; CEO</p>
      <ul class="contact__list">
        <li class="contact__item">+001 555 210 4837
          <svg class="icon" viewBox="0 0 16 16"><path d="M3.5 1l3 3-1.6 1.8a9 9 0 0 0 5.3 5.3L12 9.5l3 3-2 2.5C7 15 1 9 1 3z"/></svg>
        </li>
        <li class="contact__item">+001 555 210 4839
          <svg class="icon" viewBox="0 0 16 16"><path d="M4 1h8v4H4zM1 6h14v6h-3v3H4v-3H1zm4 4v4h6v-4z"/></svg>
        </li>
        <li class="contact__item">marlena@quorvanesensing.com
          <svg class="icon" viewBox="0 0 16 16"><path d="M1 3h14v10H1zm1.5 1.2L8 8.6l5.5-4.4z"/></svg>
        </li>
        <li class="contact__item">quorvanesensing.com
          <svg class="icon" viewBox="0 0 16 16"><circle cx="8" cy="8" r="7"/><path d="M1 8h14M8 1c-3 3-3 11 0 14M8 1c3 3 3 11 0 14" stroke="#fff" stroke-width="1" fill="none"/></svg>
        </li>
        <li class="contact__item">1180 Ridgeline Parkway
          <svg class="icon" viewBox="0 0 16 16"><path d="M8 1a5 5 0 0 1 5 5c0 4-5 9-5 9S3 10 3 6a5 5 0 0 1 5-5zm0 3a2 2 0 1 0 0 4 2 2 0 0 0 0-4z"/></svg>
        </li>
        <li class="contact__item contact__item--plain">Harlow, CO 80000</li>
      </ul>
    </div>
  </section>

</body>
</html>
```